Brackenford Hearing Clinic Business Card Design Project

We need a new business card design. We changed our logo recently and need to update our cards. We are a small hearing clinic with a 3 locations in BC. We help people with hearing loss by fitting them with hearing instruments that are appropriate for them and help them overcome the challenges that hearing loss causes. The symbol part of our logo represents the three important components of successful outcome. The three are: 1-acceptance of the change in hearing, 2-a hearing care provider that cares and is knowledgeable and experienced, 3-a quality hearing instrument. I would like to have a clean design that shows quality commitment to a successful end result of treatment. Here is our website for more information. www.earlumo.ca

Target Market(s)

Senior population - mostly 50+

Industry/Entity Type

Clinic

Requirements
Must have
• Logo
Name - Devon Pallister
Title - Hearing Instrument Practitioner (can be very small)
Phone: 250 637-4819
Address: 415-B 22nd Street, Fernhollow, BC V0R 3T5
Email: devon@earlumo.ca
website address: www.earlumo.ca
Nice to have
• Could be both sided and have a photo on the card.

```html
<!DOCTYPE html>
<html lang="en">
<head>
<meta charset="utf-8">
<title>Brackenford Hearing Clinic – Business Card</title>
<link href="https://fonts.googleapis.com/css2?family=Lato:wght@400;700;900&display=swap" rel="stylesheet">
<style>
  :root {
    --clinic-blue: #2360b0;
    --clinic-orange: #ef8b22;
    --clinic-green: #8dc63f;
    --card-white: #ffffff;
    --backdrop: #eeeae4;
    --shadow: rgba(0, 0, 0, 0.28);
  }
  * { box-sizing: border-box; margin: 0; padding: 0; }
  html, body {
    width: 1200px;
    height: 1000px;
    overflow: hidden;
    background: var(--backdrop);
    font-family: "Lato", Arial, sans-serif;
  }
  .card-set {
    position: absolute;
    top: 349px;
    left: 40px;
    display: flex;
    gap: 40px;
  }
  .card {
    position: relative;
    width: 540px;
    height: 302px;
    border-radius: 10px;
    overflow: hidden;
    box-shadow: 3px 5px 10px var(--shadow);
  }
  .card--front { background: var(--card-white); }
  .card--back {
    background: var(--clinic-blue);
    display: flex;
    align-items: center;
    justify-content: center;
  }
  .card__bands {
    position: absolute;
    inset: 0;
    width: 100%;
    height: 100%;
  }
  .band-line { fill: none; stroke-width: 5; stroke-linecap: round; }
  .band-line--orange { stroke: var(--clinic-orange); }
  .band-line--green { stroke: var(--clinic-green); }
  .band-field { fill: var(--clinic-blue); }

  .brand {
    display: flex;
    align-items: center;
    gap: 10px;
  }
  .brand__dot {
    width: 28px;
    height: 28px;
    border-radius: 50%;
    background: var(--clinic-orange);
    flex: none;
  }
  .brand__name {
    font-weight: 900;
    line-height: 1.05;
    letter-spacing: -0.3px;
  }
  .card--front .brand {
    position: absolute;
    top: 30px;
    left: 26px;
  }
  .card--front .brand__name {
    color: var(--clinic-blue);
    font-size: 20px;
    width: 160px;
  }
  .card--back .brand { gap: 12px; }
  .card--back .brand__dot {
    width: 46px;
    height: 46px;
    background: var(--card-white);
  }
  .card--back .brand__name {
    color: var(--card-white);
    font-size: 30px;
    width: 220px;
  }

  .holder {
    position: absolute;
    top: 30px;
    right: 28px;
    text-align: left;
  }
  .holder__name {
    color: var(--clinic-blue);
    font-size: 24px;
    font-weight: 700;
    line-height: 1.1;
  }
  .holder__title {
    color: var(--clinic-orange);
    font-size: 10.5px;
    margin-top: 3px;
  }

  .contacts {
    position: absolute;
    left: 19px;
    bottom: 40px;
    color: var(--card-white);
    font-weight: 700;
  }
  .contacts__row {
    display: flex;
    align-items: center;
    gap: 18px;
    font-size: 15px;
  }
  .contacts__row + .contacts__row { margin-top: 12px; }
  .contact {
    display: flex;
    align-items: center;
    gap: 6px;
  }
  .contact--address { letter-spacing: 1.1px; }
  .contact__icon { width: 18px; height: 18px; flex: none; }
  .icon-disc { fill: var(--card-white); }
  .icon-glyph { fill: var(--clinic-blue); }
  .icon-stroke { fill: none; stroke: var(--clinic-blue); stroke-width: 1.3; }
</style>
</head>
<body>
  <main class="card-set">
    <section class="card card--front" aria-label="Business card front">
      <svg class="card__bands" viewBox="0 0 540 302" preserveAspectRatio="none" aria-hidden="true">
        <path class="band-line band-line--orange" d="M-5,150 C180,150 360,112 545,104"/>
        <path class="band-line band-line--green" d="M-5,166 C180,166 360,126 545,118"/>
        <path class="band-field" d="M0,182 C180,182 360,140 540,132 L540,302 L0,302 Z"/>
      </svg>

      <div class="brand">
        <span class="brand__dot"></span>
        <span class="brand__name">Brackenford Hearing Clinic</span>
      </div>

      <div class="holder">
        <p class="holder__name">Devon Pallister</p>
        <p class="holder__title">Hearing Instrument Practitioner</p>
      </div>

      <div class="contacts">
        <div class="contacts__row">
          <span class="contact contact--phone">
            <svg class="contact__icon" viewBox="0 0 18 18" aria-hidden="true">
              <circle class="icon-disc" cx="9" cy="9" r="9"/>
              <path class="icon-glyph" d="M6,4.5 L7.6,4.5 L8.2,7 L7.2,7.8 C7.8,9.2 8.8,10.2 10.2,10.8 L11,9.8 L13.5,10.4 L13.5,12 C13.5,12.8 12.8,13.5 12,13.5 C8.3,13.2 4.8,9.7 4.5,6 C4.5,5.2 5.2,4.5 6,4.5 Z"/>
            </svg>
            250 637-4819
          </span>
          <span class="contact contact--email">
            <svg class="contact__icon" viewBox="0 0 18 18" aria-hidden="true">
              <circle class="icon-disc" cx="9" cy="9" r="9"/>
              <path class="icon-glyph" d="M4,9 L14,4.5 L11,13.5 L9,10.5 Z"/>
            </svg>
            devon@earlumo.ca
          </span>
          <span class="contact contact--web">
            <svg class="contact__icon" viewBox="0 0 18 18" aria-hidden="true">
              <circle class="icon-disc" cx="9" cy="9" r="9"/>
              <circle class="icon-stroke" cx="9" cy="9" r="5"/>
              <ellipse class="icon-stroke" cx="9" cy="9" rx="2.2" ry="5"/>
              <path class="icon-stroke" d="M4,9 H14 M5,6.5 H13 M5,11.5 H13"/>
            </svg>
            www.earlumo.ca
          </span>
        </div>
        <div class="contacts__row">
          <span class="contact contact--address">
            <svg class="contact__icon" viewBox="0 0 18 18" aria-hidden="true">
              <circle class="icon-disc" cx="9" cy="9" r="9"/>
              <path class="icon-glyph" d="M9,14.5 C7,11.8 5.5,9.8 5.5,7.8 C5.5,5.8 7,4.3 9,4.3 C11,4.3 12.5,5.8 12.5,7.8 C12.5,9.8 11,11.8 9,14.5 Z"/>
              <circle class="icon-disc" cx="9" cy="7.8" r="1.4"/>
            </svg>
            415-B 22nd Street, Fernhollow, BC V0R 3T5
          </span>
        </div>
      </div>
    </section>

    <section class="card card--back" aria-label="Business card back">
      <div class="brand">
        <span class="brand__dot"></span>
        <span class="brand__name">Brackenford Hearing Clinic</span>
      </div>
    </section>
  </main>
</body>
</html>
```